Professional window cleaning services business needs a flyer design

We are looking to attract large businesses such as gyms, car dealerships and fast food restaurants.
-Have over 15 years of experience in this business
-We serve customers in Melbourne and all surrounding suburbs
-Specialising in automated periodical services(daily,weekly,monthly, yearly)
-Our current client base consists of major fast food restaurants, car dealerships and residential properties.

Industry/Entity Type

Window Cleaning

Colors
3176b5
fbed22

Requirements
Must have
• Business Details:
• Name: Brightpane Window Cleaning
• Phone no:95402367
• website:www.quorlinpro.com.au
• email: admin@quorlinpro.com.au
• mail: PO BOX 4826, Marrowdale Heights, 3478

```html
<!DOCTYPE html>
<html lang="en">
<head>
<meta charset="utf-8">
<title>Brightpane Window Cleaning – Flyers</title>
<link rel="stylesheet" href="https://fonts.googleapis.com/css2?family=Open+Sans:wght@400;600;700&family=Questrial&family=PT+Sans+Narrow:wght@400;700&display=swap">
<style>
  :root{
    --blue:#3176b5;
    --blue-deep:#2a63a0;
    --blue-band:#2f6db0;
    --yellow:#fbed22;
    --yellow-soft:#f2e12a;
    --orange:#d8701e;
    --white:#ffffff;
    --ink-title:#1e5f9e;
    --backdrop:#e9e9ea;
  }
  *{box-sizing:border-box;margin:0;padding:0}
  html,body{width:1200px;height:803px;overflow:hidden;background:var(--backdrop)}
  .sheet-pair{position:relative;width:1200px;height:803px}
  .flyer{position:absolute;top:26px;width:480px;height:750px;background:var(--blue);overflow:hidden;font-family:"Open Sans",sans-serif;color:var(--white)}
  .flyer--services-overview{left:46px}
  .flyer--services-list{left:672px}

  .flyer__header{position:absolute;top:0;left:0;width:100%;height:60px;background:var(--white)}
  .brand-name{position:absolute;left:22px;top:16px;font-family:"Open Sans",sans-serif;font-weight:700;font-size:22px;color:var(--blue);letter-spacing:.5px}
  .flyer__title{position:absolute;right:20px;top:36px;font-family:"PT Sans Narrow",sans-serif;font-weight:700;font-size:16px;color:var(--ink-title);letter-spacing:.2px}

  .flyer__photo{position:absolute;left:0;top:60px;width:100%;height:300px}
  .flyer__curve{position:absolute;left:0;top:0;width:480px;height:750px}

  .service-columns{position:absolute;left:30px;top:394px;width:430px;display:flex;gap:16px}
  .service-col{flex:1}
  .service-col__heading{font-family:"PT Sans Narrow",sans-serif;font-size:11.5px;color:var(--yellow);text-transform:uppercase;margin-bottom:12px;white-space:nowrap}
  .service-col__heading strong{font-weight:700}
  .service-col__heading span{font-weight:400}
  .service-col p{font-size:8.3px;line-height:20px;color:var(--white)}

  .quote-line{position:absolute;left:0;width:100%;top:524px;text-align:center;font-family:"PT Sans Narrow",sans-serif;font-weight:700;font-size:17px;color:var(--yellow)}

  .divider-brand{position:absolute;left:0;width:100%;top:562px;text-align:center;font-weight:700;font-size:15px;line-height:20px;color:var(--yellow)}
  .flyer--services-list .divider-brand{top:572px}

  .call-block{position:absolute;left:38px;top:626px}
  .call-block__label{font-family:"Questrial",sans-serif;font-size:29px;color:var(--yellow);letter-spacing:.3px}
  .call-block__phone{font-family:"Questrial",sans-serif;font-size:40px;color:var(--white);margin-top:-4px;padding-left:12px}
  .flyer--services-list .call-block{top:624px}

  .contact-card{position:absolute;left:266px;top:592px;width:190px;height:150px;background:var(--orange);border:3px solid var(--white);border-radius:8px 26px 8px 8px;padding:28px 8px 0 10px;font-family:"Questrial",sans-serif;font-style:normal;font-size:10px;line-height:24px;color:var(--white);text-transform:uppercase}
  .contact-card__line{display:block;white-space:nowrap}
  .contact-card__line--post{white-space:normal;line-height:16px;margin-top:4px}
  .flyer--services-list .contact-card{left:264px;top:598px}

  .coverage-note{position:absolute;left:18px;top:712px;font-size:8.2px;color:var(--white)}

  .services-menu{position:absolute;left:148px;top:366px;width:200px;text-align:center}
  .services-menu__heading{font-family:"PT Sans Narrow",sans-serif;font-weight:700;font-size:17px;line-height:23px;color:var(--white);margin-bottom:2px}
  .services-menu ul{list-style:none}
  .services-menu li{font-family:"Questrial",sans-serif;font-size:11.4px;line-height:17.2px;color:var(--yellow-soft);text-transform:uppercase}

  .free-quote{position:absolute;left:22px;top:430px;width:150px;text-align:center;font-family:"PT Sans Narrow",sans-serif;font-weight:700;color:var(--white);transform:rotate(-8deg);line-height:18px}
  .free-quote__big{font-size:19px}
  .free-quote__small{font-size:15px}

  .experience-burst{position:absolute;left:330px;top:386px;width:120px;height:134px}
  .experience-burst__text{position:absolute;left:0;top:42px;width:100%;text-align:center;font-family:"PT Sans Narrow",sans-serif;font-weight:700;font-size:11px;line-height:12px;color:var(--blue-deep);transform:rotate(-8deg)}

  .periodic-note{position:absolute;left:0;width:100%;top:550px;text-align:center;font-size:7.8px;color:var(--white);padding-left:30px}
</style>
</head>
<body>
<main class="sheet-pair">

  <section class="flyer flyer--services-overview">
    <svg class="flyer__curve" viewBox="0 0 480 750" aria-hidden="true">
      <rect x="0" y="566" width="480" height="184" fill="var(--blue-band)"/>
      <path d="M0 578 Q240 566 480 568" stroke="var(--white)" stroke-width="3" fill="none"/>
    </svg>
    <header class="flyer__header">
      <div class="brand-name">BRIGHTPANE</div>
      <h1 class="flyer__title">BRIGHTPANE WINDOW CLEANING</h1>
    </header>
    <svg class="flyer__photo" viewBox="0 0 480 300" preserveAspectRatio="none" role="img" aria-label="Photo of a cleaner washing the glass facade of an office building with a pole, service van parked in front">
      <defs>
        <linearGradient id="facadeTone" x1="0" y1="0" x2="0" y2="1">
          <stop offset="0" stop-color="#cfdde9"/>
          <stop offset=".45" stop-color="#6f8496"/>
          <stop offset=".8" stop-color="#54605a"/>
          <stop offset="1" stop-color="#4b5a46"/>
        </linearGradient>
      </defs>
      <rect width="480" height="300" fill="url(#facadeTone)"/>
      <path d="M0 300 L0 282 Q240 240 480 272 L480 300 Z" fill="var(--blue)"/>
    </svg>

    <div class="service-columns">
      <div class="service-col">
        <h2 class="service-col__heading"><strong>Residential</strong> <span>Window Cleaning</span></h2>
        <p>Clean windows at home makes for a perfect view. Keep your windows clean all year round with Brightpane Window Cleaning</p>
      </div>
      <div class="service-col">
        <h2 class="service-col__heading"><strong>Commercial</strong> <span>Window Cleaning</span></h2>
        <p>Brightpane Window Cleaning services different commercial properties including shops, offices, schools, hotels, nursing homes and hospitals throughout Melbourne.</p>
      </div>
      <div class="service-col">
        <h2 class="service-col__heading"><strong>Real Estate</strong> <span>Window Cleaning</span></h2>
        <p>Many Real Estate Agents and Body Corporates rely on Brightpane Window Cleaning. We can set up a maintenance program to suit your needs.</p>
      </div>
    </div>

    <p class="quote-line">FREE WINDOW CLEANING QUOTE</p>
    <div class="divider-brand">BRIGHTPANE</div>

    <div class="call-block">
      <p class="call-block__label">CALL US TODAY</p>
      <p class="call-block__phone">9540 2367</p>
    </div>
    <address class="contact-card">
      <span class="contact-card__line">www.quorlinpro.com.au</span>
      <span class="contact-card__line">admin@quorlinpro.com.au</span>
      <span class="contact-card__line contact-card__line--post">PO Box 4826, Marrowdale Heights, 3478</span>
    </address>
  </section>

  <section class="flyer flyer--services-list">
    <svg class="flyer__curve" viewBox="0 0 480 750" aria-hidden="true">
      <rect x="0" y="582" width="480" height="168" fill="var(--blue-band)"/>
      <path d="M0 592 Q240 580 480 582" stroke="var(--white)" stroke-width="3" fill="none"/>
    </svg>
    <header class="flyer__header">
      <div class="brand-name">BRIGHTPANE</div>
      <h1 class="flyer__title">BRIGHTPANE WINDOW CLEANING</h1>
    </header>
    <svg class="flyer__photo" viewBox="0 0 480 300" preserveAspectRatio="none" role="img" aria-label="Photo of the yellow company service van with ladders on the roof parked beside a road">
      <defs>
        <linearGradient id="vanTone" x1="0" y1="0" x2="0" y2="1">
          <stop offset="0" stop-color="#c9d6e4"/>
          <stop offset=".4" stop-color="#9aa7a4"/>
          <stop offset=".6" stop-color="#d9c94a"/>
          <stop offset=".85" stop-color="#6d7063"/>
          <stop offset="1" stop-color="#7a7c78"/>
        </linearGradient>
      </defs>
      <rect width="480" height="300" fill="url(#vanTone)"/>
      <path d="M0 300 L0 268 Q240 236 480 252 L480 300 Z" fill="var(--blue)"/>
    </svg>

    <div class="free-quote">
      <div class="free-quote__big">FREE</div>
      <div class="free-quote__small">WINDOW CLEANING</div>
      <div class="free-quote__small">QUOTE</div>
    </div>

    <div class="services-menu">
      <h2 class="services-menu__heading">SERVICES</h2>
      <ul>
        <li>High Rise Services</li>
        <li>Residential Services</li>
        <li>Corporate Services</li>
        <li>Commercial Services</li>
        <li>Gutter Services</li>
        <li>Roof Services</li>
        <li>Pressure Services</li>
        <li>Blind Services</li>
        <li>Consulting Services</li>
      </ul>
    </div>

    <div class="experience-burst">
      <svg viewBox="0 0 120 134" width="120" height="134" aria-hidden="true">
        <polygon fill="var(--yellow)" points="78,0 76,40 120,30 88,62 118,90 80,84 86,134 60,96 30,124 38,86 0,84 30,62 6,34 44,42 50,6 62,38"/>
      </svg>
      <div class="experience-burst__text">OVER<br>15 YEARS OF<br>EXPERIENCE</div>
    </div>

    <p class="periodic-note">Specialising in automated periodical services ( daily,weekly,monthly, yearly )</p>
    <div class="divider-brand">BRIGHTPANE</div>

    <div class="call-block">
      <p class="call-block__label">CALL US TODAY</p>
      <p class="call-block__phone">9540 2367</p>
    </div>
    <p class="coverage-note">We serve customers in Melbourne and all surrounding suburbs</p>
    <address class="contact-card">
      <span class="contact-card__line">www.quorlinpro.com.au</span>
      <span class="contact-card__line">admin@quorlinpro.com.au</span>
      <span class="contact-card__line contact-card__line--post">PO Box 4826, Marrowdale Heights, 3478</span>
    </address>
  </section>

</main>
</body>
</html>
```